Post Card Design - Photo on front, details on back. Logo on both sides.

Back: See the photo of my old card. The back worked well, as it gave me lots of space to write on. The address details are still correct, but the logo has changed to Josephine Sans. Logo can be on one line or on two (if two, align it on the left).
Don't include the 'BEAUTIFUL WEDDING DRESSES...' bit.
I'd like to print this on thicker, slightly coarse paper, so don't go too small on detail.
Here are the Plume paper details: Paper Stock: Natural Uncoated
Paper Thickness: Premium
Finish: None
Front of Card: I'd like to see options for both pictures:
I think the painted image would look best with a frame in a pale shade and the logo in the frame fairly subtle.
The actual dress photo I'd like to see cropped a bit like in my mock up. You'll need to have a look at how the logo would be best placed on this. You can place it anywhere, or add a banner.
See my website for my brand's look: mirabeltoft.co.nz
Target Market(s)
Brides
Industry/Entity Type
Wedding Dresses
Contact Information for Business Card
Front: Photo and logo. Back: with details and lots of empty space. See attached photos for loose brief.
Other font styles liked:
- Josephine Sans
Requirements
Must have
- I hand-write the gown designs and price on the back of the card, so there needs to be plenty of empty space.
Nice to have
- As per brief.
Should not have
- It must look clean, romantic, modern. Timeless.

```html
<!DOCTYPE html>
<html lang="en">
<head>
<meta charset="utf-8">
<title>Mirabel Toft – Post Card</title>
<link rel="stylesheet" href="https://fonts.googleapis.com/css2?family=Josefin+Sans:wght@100;300;400&family=Open+Sans:wght@400&display=swap">
<style>
  :root {
    --bg: #ededed;
    --card: #ffffff;
    --ink: #2b2b2b;
    --band: #b7b9bc;
    --band-ink: #4f5155;
    --photo-light: #efe2cf;
    --photo-mid: #d9c3a4;
    --photo-deep: #b89d7c;
    --logo-light: #ffffff;
  }
  * { margin: 0; padding: 0; box-sizing: border-box; }
  html, body { width: 1200px; height: 900px; overflow: hidden; background: var(--bg); }
  .canvas { position: relative; width: 1200px; height: 900px; }

  .card-front {
    position: absolute; left: 100px; top: 58px; width: 553px; height: 367px;
    overflow: hidden;
  }
  .dress-photo {
    position: absolute; inset: 0;
    background:
      linear-gradient(90deg, rgba(255,255,255,0.55) 0%, rgba(255,255,255,0) 30%),
      linear-gradient(180deg, var(--photo-mid) 0%, var(--photo-light) 45%, var(--photo-deep) 70%, var(--photo-light) 100%);
  }
  .front-logo {
    position: absolute; right: 372px; top: 30px;
    writing-mode: vertical-rl;
    font-family: "Josefin Sans", sans-serif;
    font-weight: 100;
    color: var(--logo-light);
    line-height: 1;
    text-transform: uppercase;
  }
  .front-logo .first { font-size: 70px; letter-spacing: 4px; }
  .front-logo .last { font-size: 48px; letter-spacing: 28px; margin-right: 4px; }

  .card-back {
    position: absolute; left: 546px; top: 475px; width: 554px; height: 365px;
    background: var(--card);
  }
  .back-logo {
    position: absolute; left: 52px; top: 52px;
    font-family: "Josefin Sans", sans-serif;
    font-weight: 300; font-size: 25px; letter-spacing: 1.5px;
    color: var(--ink); text-transform: uppercase;
  }
  .contact-band {
    position: absolute; left: 0; bottom: 0; width: 100%; height: 55px;
    background: var(--band);
    display: flex; align-items: center; gap: 14px;
    padding-left: 52px;
    font-family: "Open Sans", sans-serif; font-size: 13.5px; color: var(--band-ink);
  }
  .contact-item { display: flex; align-items: center; gap: 3px; }
  .contact-item svg { width: 11px; height: 11px; flex: none; }
</style>
</head>
<body>
<div class="canvas">
  <section class="card-front">
    <div class="dress-photo" role="img" aria-label="Photograph of a bride in a white gown with a flowing veil in a sunlit stone hallway"></div>
    <div class="front-logo">
      <span class="first">Mirabel</span><br>
      <span class="last">Toft</span>
    </div>
  </section>

  <section class="card-back">
    <div class="back-logo">Mirabel Toft</div>
    <div class="contact-band">
      <span class="contact-item">
        <svg viewBox="0 0 12 12" aria-hidden="true"><path d="M3 1 L4.8 3.6 L3.8 4.8 Q5 7.2 7.2 8.2 L8.4 7.2 L11 9 L9.8 11 Q4.5 10.5 1 3.2 Z" fill="currentColor"/></svg>
        +64 9 555 0142
      </span>
      <span class="contact-item">
        <svg viewBox="0 0 12 12" aria-hidden="true" fill="none" stroke="currentColor" stroke-width="1"><circle cx="6" cy="6" r="5"/><ellipse cx="6" cy="6" rx="2.2" ry="5"/><line x1="1" y1="6" x2="11" y2="6"/></svg>
        mirabeltoft.co.nz
      </span>
      <span class="contact-item">
        <svg viewBox="0 0 12 12" aria-hidden="true" fill="none" stroke="currentColor" stroke-width="1"><rect x="1" y="2.5" width="10" height="7"/><path d="M1 2.5 L6 6.5 L11 2.5"/></svg>
        hello@mirabeltoft.co.nz
      </span>
    </div>
  </section>
</div>
</body>
</html>
```